PowerPoint Design Project

Hi,

Using our logo, we would like a designer to provide us with a powerpoint template that has a unique brand.

To us this means creating a color palette, treatment, a font that plays off of our logo. The color palette needs to blend well with our existing colors, but give us some options, make things "POP".

The color palette needs to include the colors (with RGB numbers), gradients, different graphic styles (solid, transparent, gradient, image fills) and lines (a callout leader line, a multi-color bar to divide content)

The palette and treatment must extend itself to graphs, charts and images.

We would also like to see different parts of our logo applied to the different template slides. For example, on a title slide we would like the image with our logo and tagline. With the end slide we would like to see our logo and URL. We also attached our logo without the tagline and also just the colored cube. So please be creative on how these are incorporated into the deck.

Images are attached.

Thank you
Carlton

Target Market(s)

Large Corporations

Requirements
Must have
• color palette, treatments and consistent fonts. color palette must complement our logo. color palette must extend to graphs, charts and images.

different logo's incorprated into the deck. For example, on a title slide we would like the image with our logo and tagline. With the end slide we would like to see our logo and URL. We also attached our logo without the tagline and also just the colored cube. So please be creative on how these are incorporated into the deck.
Should not have
• We do not want to see designers taking the logo and incorporating them into the background and calling it a template.

```html
<!DOCTYPE html>
<html lang="en">
<head>
<meta charset="utf-8">
<title>veltragroup – presentation template</title>
<link rel="stylesheet" href="https://fonts.googleapis.com/css2?family=Fira+Sans:wght@400;500;600&display=swap">
<style>
  :root {
    --page: #ffffff;
    --ink: #231f20;
    --brand-green: #8dc63f;
    --brand-blue: #1d5fa8;
    --teal: #3aaec6;
    --violet-top: #cf5ee0;
    --violet-bottom: #4e0f5c;
    --violet-word: #f068ff;
    --sky-word: #5ccbf7;
    --mist-top: #f5f6f9;
    --mist-bottom: #dde1ea;
    --rule: #c9ceda;
    --body: #2d2d33;
    --footer-top: #4a4d56;
    --footer-bottom: #24262b;
    --faint: #c4c8d0;
  }
  * { box-sizing: border-box; margin: 0; padding: 0; }
  html, body { width: 1200px; height: 905px; overflow: hidden; background: var(--page); }
  body { position: relative; font-family: "Fira Sans", sans-serif; }

  .slide { position: absolute; width: 581px; height: 436px; overflow: hidden; }
  .slide--title   { left: 14px;  top: 10px;  background: linear-gradient(var(--mist-top), var(--mist-bottom)); }
  .slide--analyze { left: 605px; top: 10px;  width: 582px; background: linear-gradient(var(--violet-top), var(--violet-bottom)); }
  .slide--content { left: 14px;  top: 457px; background: linear-gradient(#fbfbfd, #e3e6ee); }
  .slide--elevate { left: 605px; top: 457px; width: 582px; background: linear-gradient(#3fb0c8, #0f63ae); }

  /* title slide */
  .brand { position: absolute; left: 94px; top: 172px; display: flex; align-items: center; gap: 16px; }
  .brand__mark { width: 88px; height: 88px; background: var(--brand-blue); flex: none; }
  .brand__text { display: flex; flex-direction: column; }
  .brand__name { font-size: 50px; font-weight: 500; color: var(--ink); line-height: 1.08; letter-spacing: -0.5px; }
  .brand__tagline { font-size: 14px; color: var(--brand-blue); letter-spacing: 0.3px; line-height: 1.2; margin: 4px 0 0 3px; }

  /* section divider slides */
  .section-word { position: absolute; left: 92px; top: 180px; display: flex; align-items: center; gap: 22px; }
  .section-word__mark { width: 76px; height: 76px; }
  .section-word__text { font-size: 66px; font-weight: 500; line-height: 1; }
  .slide--analyze .section-word__mark { background: var(--violet-word); }
  .slide--analyze .section-word__text { color: var(--violet-word); }
  .slide--elevate .section-word__mark { background: var(--sky-word); }
  .slide--elevate .section-word__text { color: var(--sky-word); }

  /* content slide */
  .content__topbar { position: absolute; left: 0; top: 0; width: 100%; height: 5px; background: var(--teal); }
  .content__heading { position: absolute; left: 8px; top: 11px; font-size: 21px; font-weight: 400; color: var(--teal); line-height: 1.1; }
  .content__rule { position: absolute; left: 0; top: 38px; width: 280px; height: 2px; background: var(--rule); }
  .content__brand { position: absolute; left: 292px; top: 26px; display: flex; align-items: center; gap: 8px; }
  .content__brand-mark { width: 22px; height: 22px; background: var(--faint); }
  .content__brand-name { font-size: 19px; color: var(--faint); }

  .content__photo { position: absolute; left: 33px; top: 55px; width: 194px; height: 338px;
    background: linear-gradient(180deg, #d9dde6 0%, #2a3140 45%, #161b26 100%); }

  .points { position: absolute; left: 258px; top: 72px; width: 300px; }
  .points__title { font-size: 12px; font-weight: 600; color: var(--teal); margin: 0 0 11px 26px; line-height: 1.2; }
  .points__item { position: relative; padding-left: 25px; font-size: 8.6px; line-height: 12.4px; color: var(--body); margin-bottom: 15px; }
  .points__item::before { content: ""; position: absolute; left: 0; top: 2px; width: 9px; height: 9px; border-radius: 50%;
    background: linear-gradient(135deg, var(--brand-green) 50%, var(--brand-blue) 50%); }
  .points__item b { font-weight: 600; color: var(--ink); }
  .points__divider { height: 1px; background: var(--rule); margin: 6px 10px 18px 18px; }

  .footer { position: absolute; left: 0; bottom: 0; width: 100%; height: 43px; background: linear-gradient(var(--footer-top), var(--footer-bottom));
    display: flex; align-items: center; font-size: 8.6px; color: var(--brand-green); }
  .footer__page { position: absolute; left: 14px; }
  .footer__contact { position: absolute; left: 185px; display: flex; align-items: center; gap: 16px; }
  .footer__mark { width: 22px; height: 22px; background: var(--brand-green); }
</style>
</head>
<body>

  <section class="slide slide--title">
    <div class="brand">
      <div class="brand__mark"></div>
      <div class="brand__text">
        <div class="brand__name">veltragroup</div>
        <div class="brand__tagline">analyze . elevate . transform</div>
      </div>
    </div>
  </section>

  <section class="slide slide--analyze">
    <div class="section-word">
      <div class="section-word__mark"></div>
      <div class="section-word__text">analyze</div>
    </div>
  </section>

  <section class="slide slide--content">
    <div class="content__topbar"></div>
    <h2 class="content__heading">analyze</h2>
    <div class="content__rule"></div>
    <div class="content__brand">
      <div class="content__brand-mark"></div>
      <div class="content__brand-name">veltragroup</div>
    </div>

    <div class="content__photo" role="img" aria-label="Portrait photo of a businessman in a dark suit standing with hands clasped"></div>

    <div class="points">
      <h3 class="points__title">Analyze</h3>
      <p class="points__item">Aenean ridiculus <b>tortor</b> quis interdum id habitant ad, natoque consectetuer nisl auctor libero quisque euismod ante inceptos malesuada ligula mattis.</p>
      <p class="points__item"><b>Nulla,</b> netus pulvinar pellentesque porttitor purus maecenas tellus hac nulla lacus. Lorem. Nostra laoreet nulla, dis cursus nascetur dolor odio Eu Magna molestie montes dui mus cursus habitasse mauris tempor.</p>
      <p class="points__item">Varius inceptos nascetur mollis dui aptent ultrices. Pretium pulvinar ante lobortis convallis lectus netus vitae penatibus eros at blandit. Parturient.</p>
      <div class="points__divider"></div>
      <h3 class="points__title">Elevate</h3>
      <p class="points__item">Aenean ridiculus <b>tortor</b> quis interdum id habitant ad, natoque consectetuer nisl auctor libero quisque euismod ante inceptos malesuada ligula mattis.</p>
      <p class="points__item"><b>Nulla,</b> netus pulvinar pellentesque porttitor purus maecenas tellus hac nulla lacus. Lorem. Nostra laoreet nulla, dis cursus nascetur dolor odio</p>
    </div>

    <footer class="footer">
      <span class="footer__page">3</span>
      <div class="footer__contact">
        <span>info@veltragroup.com</span>
        <span class="footer__mark"></span>
        <span>www.veltragroup.com</span>
      </div>
    </footer>
  </section>

  <section class="slide slide--elevate">
    <div class="section-word">
      <div class="section-word__mark"></div>
      <div class="section-word__text">elevate</div>
    </div>
  </section>

</body>
</html>
```